Business Card Design and Stationary design for consulting firm

Harbourline Sourcing are looking for a new business card design and a design for their A4 letterhead / A4 invoices.

We are seeking to heavily increase our brand awareness and require a business card that's professional in appearance but also shows flare and innovation. A card design that people will remember.

About Us
Harbourline Sourcing are `The Sourcing Crew’.
Our mission is to be one of Australia’s greatest companies. Our aim is to help our customers achieve the best result from their purchasing experience.

Our Requirement:
• IMPACT! IMPACT! IMPACT!
• BUSINESS & PROFESSIONAL LOOKING

• Our business colours are orange, blue and green (See the logo attached).

We have provided an Art Design specification (attached) that needs to be followed for you to win the design. This also has the font, which is used on the logo.

We are after a two sided business card

Side One should have the:
The company Logo
The Sourcing Crew
www.harbourlinesourcing.com.au
Procure | Personnel | Probity & Privacy
Sydney | Melbourne | Adelaide | Brisbane

Side Two
Logo (optional)
Harbourline Sourcing (optional)
Employee details (details listed below)

The above format is our preferred option, but if you think you can come up with something better, feel free to put it forward.

We are leaving the design up to you, but it must incorporate the logo.

We will need a template that we can change the employee details on, as we will be adding more staff over the coming months.

The details below are for one employee per card with the same design.
------------------------

Employee Details:

Marcus Del Arroyo MBA, MMgmtStratProc
Principal Consultant
0491 372 618
Marcus@harbourlinesourcing.com.au

Brianna Tolley
Consulting Manager
0462 915 308
Brianna@harbourlinesourcing.com.au

Our website is www.harbourlinesourcing.com.au

The Letterhead / invoice needs to incorporate:
the company Logo
The Sourcing Crew
Sydney | Melbourne | Adelaide | Brisbane but otherwise the design is over to you.

This file needs to be delivered in word format as other detail will be added to the documents.

We look forward to you award winning designs. If you require any further information please feel free to contact us.

Regards
Harbourline Sourcing

Target Market(s)

Our Target market is companies with 80+ employees. The market we segment is heavily male based, between the ages of 35-55 years of age.

Industry/Entity Type

Consulting

Contact Information for Business Card

See Project Description

Font styles to use
Other font styles liked:
• See Art Specification

Requirements
Must have
• Company Colours, See Project Description
Should not have
• Be outside the Art specification guidelines

```html
<!DOCTYPE html>
<html lang="en">
<head>
<meta charset="utf-8">
<title>Harbourline Sourcing – Business Card</title>
<link href="https://fonts.googleapis.com/css2?family=Arimo:wght@400;700&family=Tinos:wght@400;700&display=swap" rel="stylesheet">
<style>
  :root{
    --stage:#e9e7e3;
    --card:#f4f4f4;
    --ink:#4a4a4a;
    --ink-soft:#8a8a8a;
    --panel-light:#7b7b7b;
    --panel-dark:#4b4b4b;
    --panel-edge:#a9a9a9;
    --on-panel:#f2f2f2;
    --accent:#2f86c9;
  }
  *{margin:0;padding:0;box-sizing:border-box}
  html,body{width:1200px;height:902px;overflow:hidden;background:var(--stage)}
  .canvas{position:relative;width:1200px;height:902px}
  .card{
    position:absolute;left:280px;width:640px;height:366px;
    background:var(--card);overflow:hidden;
    box-shadow:0 6px 18px rgba(0,0,0,.18);
  }
  .card--front{top:68px}
  .card--back{top:468px}

  .brand{display:flex;align-items:center;gap:12px}
  .brand__dot{width:26px;height:26px;border-radius:50%;background:var(--accent)}
  .brand__name{font-family:"Arimo",sans-serif;font-weight:700;color:var(--ink);letter-spacing:.02em}

  .card--front .brand{position:absolute;left:0;right:0;top:130px;justify-content:center}
  .card--front .brand__name{font-size:40px}
  .web{
    position:absolute;left:40px;right:40px;top:262px;
    display:flex;align-items:center;gap:16px;
    font-family:"Tinos",serif;font-size:19px;color:var(--ink);letter-spacing:.04em;
  }
  .web::before,.web::after{content:"";flex:1;height:3px;background:var(--ink-soft)}

  .panels{position:absolute;inset:0}
  .card--back .brand{position:absolute;left:24px;top:200px;gap:10px}
  .card--back .brand__dot{width:18px;height:18px;flex:none}
  .card--back .brand__name{font-size:19px;white-space:nowrap;letter-spacing:0}

  .person{position:absolute;right:26px;text-align:right;color:var(--on-panel);font-family:"Arimo",sans-serif;white-space:nowrap}
  .person--lead{top:20px}
  .person--second{top:214px}
  .person__name{font-family:"Tinos",serif;font-weight:700;font-size:24px;line-height:1.1}
  .person__role{font-size:14px;line-height:1.3}
  .person__contact{margin-top:10px;font-size:14px;line-height:1.45}
  .line{display:flex;justify-content:flex-end;align-items:center;gap:8px}
  .icon{width:13px;height:13px;flex:none}
</style>
</head>
<body>
<main class="canvas">
  <section class="card card--front">
    <div class="brand"><span class="brand__dot"></span><span class="brand__name">Harbourline Sourcing</span></div>
    <p class="web">www.harbourlinesourcing.com.au</p>
  </section>

  <section class="card card--back">
    <svg class="panels" width="640" height="366" viewBox="0 0 640 366">
      <polygon points="200,0 640,0 640,150 310,214" fill="var(--panel-light)"/>
      <polygon points="310,214 640,150 640,366 310,366" fill="var(--panel-dark)"/>
      <polyline points="190,0 300,214 300,366" fill="none" stroke="var(--panel-edge)" stroke-width="6"/>
    </svg>

    <div class="brand"><span class="brand__dot"></span><span class="brand__name">Harbourline Sourcing</span></div>

    <div class="person person--lead">
      <p class="person__name">Marcus Del Arroyo</p>
      <p class="person__role">MBA, MMgmtStratProc</p>
      <p class="person__role">Principal Consultant</p>
      <div class="person__contact">
        <p class="line">0491 372 618
          <svg class="icon" viewBox="0 0 14 14"><rect width="14" height="14" fill="var(--on-panel)"/><path d="M4 3h2l1 3-1.5 1a6 6 0 0 0 2.5 2.5L9 8l3 1v2c-5 0-8-3-8-8z" fill="var(--panel-light)"/></svg></p>
        <p class="line">Marcus@harbourlinesourcing.com.au
          <svg class="icon" viewBox="0 0 14 14"><rect width="14" height="14" fill="var(--on-panel)"/><rect x="2.5" y="4" width="9" height="6" fill="none" stroke="var(--panel-light)"/><path d="M2.5 4l4.5 3.5L11.5 4" fill="none" stroke="var(--panel-light)"/></svg></p>
      </div>
    </div>

    <div class="person person--second">
      <p class="person__name">Brianna Tolley</p>
      <p class="person__role">Consulting Manager</p>
      <div class="person__contact">
        <p class="line">0462 915 308
          <svg class="icon" viewBox="0 0 14 14"><rect width="14" height="14" fill="var(--on-panel)"/><path d="M4 3h2l1 3-1.5 1a6 6 0 0 0 2.5 2.5L9 8l3 1v2c-5 0-8-3-8-8z" fill="var(--panel-dark)"/></svg></p>
        <p class="line">Brianna@harbourlinesourcing.com.au
          <svg class="icon" viewBox="0 0 14 14"><rect width="14" height="14" fill="var(--on-panel)"/><rect x="2.5" y="4" width="9" height="6" fill="none" stroke="var(--panel-dark)"/><path d="M2.5 4l4.5 3.5L11.5 4" fill="none" stroke="var(--panel-dark)"/></svg></p>
      </div>
    </div>
  </section>
</main>
</body>
</html>
```